Flyer for Compassion training days

I need a A5-size, single-sided flyer design for my training days. They are weekends in a blend of Compassionate Communication and Buddhist teachings called Palomere Communication. The logo for Palomere that should be included.
The flyer needs room for 1) course title, 2) course dates, location & price, 3) course description, 4) booking info, 5) my picture & short bio, and 6) the palomere.co website (yes, it is 'co' and not 'com).
Updates

Target Market(s)

Women 35-65 years, well-educated, spiritually minded. May have interests like yoga and meditation.

Industry/Entity Type

Health And Wellness

Font styles to use
Sans Serif
Other font styles liked:
• Blue Plaque, Josefina are both great

Colors
fbf289
fdf9cf
cfeae6
33b8a4

Requirements
Must have
• The Palomere logo; my picture.
• Elegance. Calm and expansive feel.
• The poster provided in the project files shows you the kind of information I need to include.
• Colours -- greens and yellows, but the options on pixel harbor are not quite the right shades.
• The logo colour can be changed.
Nice to have
• Classy (but not cliche) image associated with Buddhism; gentle curves similar to those on the business card (see project files).
Should not have
• Dark background. Busy, loud design. Overly 'swirly' design. Images that I have to buy separately.

```html
<!DOCTYPE html>
<html lang="en">
<head>
<meta charset="utf-8">
<title>Palomere Communication Core Course – Flyer</title>
<link href="https://fonts.googleapis.com/css2?family=Josefin+Sans:wght@300;400;600;700&display=swap" rel="stylesheet">
<style>
  :root{
    --page-bg:#ecebe6;
    --cream:#fdf9cf;
    --yellow:#fbf289;
    --mint:#cfeae6;
    --teal:#33b8a4;
    --green:#17a34a;
    --brown:#6b3a2c;
    --title:#8a3b32;
    --text:#5a4234;
    --gold-light:#f0d48a;
    --gold-dark:#9a7420;
  }
  *{box-sizing:border-box;margin:0;padding:0}
  html,body{width:1200px;height:1200px;overflow:hidden}
  body{background:var(--page-bg);font-family:"Josefin Sans",sans-serif;color:var(--text)}
  .flyer{position:absolute;left:190px;top:20px;width:820px;height:1160px;background:var(--cream);overflow:hidden;box-shadow:0 4px 18px rgba(0,0,0,.12)}
  .landscape{position:absolute;left:0;top:0;width:100%;height:520px;
    background:linear-gradient(180deg,#eef2f3 0%,#dfe4e0 30%,#b9bea4 62%,rgba(253,249,207,0) 100%)}
  .brand{position:absolute;right:48px;top:44px;display:flex;align-items:center;gap:10px;font-size:30px;font-weight:600;color:var(--green)}
  .brand-dot{width:22px;height:22px;border-radius:50%;background:var(--green)}
  .tagline{position:absolute;left:60px;top:88px;font-size:30px;font-weight:400;color:var(--brown);line-height:1.15}
  .tagline .plus{color:var(--green)}
  .title{position:absolute;left:60px;top:178px;font-size:52px;font-weight:700;color:var(--title);line-height:1.1;letter-spacing:.5px}
  .statue{position:absolute;right:20px;top:200px;width:220px;height:420px;border-radius:110px 110px 40px 40px;
    background:radial-gradient(ellipse at 45% 35%,var(--gold-light) 0%,#c79d3c 55%,var(--gold-dark) 100%)}
  .details-band{position:absolute;left:0;top:460px;width:100%;height:150px;background:var(--yellow)}
  .details{position:absolute;left:60px;top:478px;font-size:34px;font-weight:600;color:var(--brown);line-height:1.12}
  .price{display:block;margin-top:10px;font-size:28px;color:var(--green)}
  .description{position:absolute;left:60px;top:636px;width:470px;font-size:17px;font-weight:300;line-height:1.35}
  .explore{position:absolute;left:60px;top:742px;width:720px;font-size:18px}
  .explore h2{font-size:18px;font-weight:600;color:var(--brown);margin-bottom:6px}
  .explore ul{list-style:none}
  .explore li{display:flex;align-items:center;gap:10px;color:var(--title);font-weight:400;line-height:1.5}
  .explore li::before{content:"";width:12px;height:12px;border-radius:50%;background:var(--green);flex:none}
  .audience{position:absolute;left:60px;top:892px;width:720px;font-size:17px;line-height:1.3;color:var(--brown)}
  .booking{position:absolute;left:60px;top:978px;font-size:20px;color:var(--green);white-space:nowrap}
  .booking strong{font-weight:700}
  .booking .email{color:var(--brown);font-weight:600}
  .facilitator-band{position:absolute;left:0;top:1020px;width:100%;height:140px;background:var(--mint)}
  .portrait{position:absolute;left:60px;top:1032px;width:105px;height:118px;border:2px solid var(--green);
    background:linear-gradient(160deg,#c9b08a,#8b6d48)}
  .bio{position:absolute;left:190px;top:1036px;width:570px;font-size:16px;line-height:1.3;color:var(--brown)}
  .coaching{position:absolute;left:190px;top:1106px;font-size:16px;color:var(--green);line-height:1.2;text-transform:uppercase}
  .coaching strong{font-weight:600}
  .website{position:absolute;right:48px;top:1116px;font-size:22px;font-weight:700;color:var(--green)}
</style>
</head>
<body>
  <main class="flyer">
    <div class="landscape" role="img" aria-label="Soft misty landscape photograph of wooded hills"></div>

    <div class="brand"><span class="brand-dot"></span>Palomere</div>

    <p class="tagline">Mindfulness <span class="plus">+</span> Kindness <span class="plus">+</span><br>Compassionate Communication =</p>
    <h1 class="title">PALOMERE<br>COMMUNICATION<br>CORE<br>COURSE</h1>

    <div class="details-band"></div>
    <div class="statue" role="img" aria-label="Photograph of a golden resting Buddha statue holding a small flower"></div>
    <p class="details">11-12 Dec<br>Thistlebank Centre, Edinburgh<span class="price">(£125/100)</span></p>

    <p class="description">Palomere Communication can help you increase awareness &amp; compassion in everyday speech (with yourself &amp; others), better understand your own patterns, and build resilience to challenging situations. Choose from:</p>

    <section class="explore">
      <h2>In this 2-day Core Course, we’ll explore:</h2>
      <ul>
        <li>Compassionate Communication;</li>
        <li>Buddhist teachings on Right Speech, loving-kindness, Right Effort, and more;</li>
        <li>Mindfulness practices;</li>
        <li>Choices available to us in our everyday speech.</li>
      </ul>
    </section>

    <p class="audience">This workshop will be of interest if you’d like to improve personal and/or professional relationships. Open to all, best suited to those with at least 1 year’s experience with Mindfulness, Buddhism, or Compassionate Communication / NVC.</p>

    <p class="booking"><strong>BOOKING:</strong> Book online at TicketMeadow or write <span class="email">maribeth@palomere.co</span></p>

    <div class="facilitator-band"></div>
    <div class="portrait" role="img" aria-label="Sepia portrait photograph of the facilitator"></div>
    <p class="bio">Facilitator: Maribeth Ellwood is an experienced group facilitator, having worked with a range of organisations and presented at a number of festivals &amp; conferences.</p>
    <p class="coaching">Maribeth offers coaching in<br><strong>Palomere Communication.</strong></p>
    <p class="website">www.palomere.co</p>
  </main>
</body>
</html>
```